Brightmoor Paving Stationery Design COMMITTED PAY

We need you to design stationary for a new Business called Brightmoor Paving. We have already got the logo designed and it is attached. Obviously we're looking for a stationery set designed around the colours and style to match the logo.

Use generic name, address, phone, fax, email etc ... I will edit text to required details.

What we need:
- Business Card Design Double Sided (90 x 55m + Bleed 3mm+)
- A4 Letter head Design
- A4 Presentation Folder Design
- Invoice Header Approx 210 x 55mm (Include Logo & Images)

And whatever other bonuses you'd like to kick in associated with the package.

I've attached some images and I've got hundreds more. If you want something else in the way of images, let me know.

I look forward to your seeing your designs.
Updates

Thought I should just clarify the follwoing:

1. The Invoice Header is just a branding for the top of my accounting package form.  It is not contain any contact information or the like.  Just logo, some images and some of your creativity and flair to bring it together.
2. The business does synthetic grass (75% of the business), Wetpour Rubber Surfaces, Softfall Surfaces and Rubber Wood Mulch.  These are categories you might choose to somehow highlight on the letterhead.
3. Business Card reverse side should be used to highlight the categories using images provided.

Wow, I've had some really nice designs submitted thus far, but my concern is that I can't just have an awesome looking card.  I really feel that my card needs to either show or say what we do.  Please make sure your design either shows or says the following:

- Synthetic Grass
- Wetpour Rubber Surfaces
- Softfall Surfaces
- Rubber Wood Mulch
- Shade Structures
- Landscape Structures

Just another note, don't know if I mentioned it or not in the original brief, but I prefer the use of icons instead of text for phone, email, fax etc labels.

Industry/Entity Type

Business

Requirements
Must have
• - Provide full editable source files
- Provide letterhead in MS Word format as well
- All designs must be awesome, but also show or say what we do. This is very important to me. I want anyone to look at our letterhead, business card etc and know instantly what it is that we do.
- Super quick turnaround on handover. I need card files to the printer on Monday morning (that's my Monday at GMT+10)
Nice to have
• - Creative use of the logo for a little bit of wow
Should not have
• - not square, boxy or rigid ... Loosen up a bit!

```html
<!DOCTYPE html>
<html lang="en">
<head>
<meta charset="utf-8">
<title>Brightmoor Paving Letterhead</title>
<link href="https://fonts.googleapis.com/css2?family=Source+Sans+3:wght@400;700&display=swap" rel="stylesheet">
<style>
  :root {
    --brand-blue: #1b9ddb;
    --brand-green: #8dc63f;
    --green-light: #b5d975;
    --ink: #1a1a1a;
    --paper: #ffffff;
  }
  html, body {
    margin: 0;
    padding: 0;
    overflow: hidden;
    background: var(--paper);
  }
  .letterhead {
    position: relative;
    width: 927px;
    height: 1200px;
    overflow: hidden;
    background: var(--paper);
    font-family: "Source Sans 3", sans-serif;
    color: var(--ink);
  }
  .brand {
    position: absolute;
    left: 46px;
    top: 40px;
    display: flex;
    align-items: center;
    gap: 14px;
  }
  .brand-mark {
    width: 68px;
    height: 68px;
    border-radius: 50%;
    background: var(--brand-green);
    flex: none;
  }
  .brand-text {
    display: flex;
    flex-direction: column;
  }
  .brand-name {
    font-weight: 700;
    font-size: 37px;
    line-height: 1;
    color: var(--brand-blue);
    text-transform: uppercase;
  }
  .brand-tagline {
    margin-top: 5px;
    font-weight: 700;
    font-size: 17px;
    color: var(--brand-blue);
  }
  .contact {
    position: absolute;
    left: 732px;
    top: 44px;
    font-size: 15px;
    font-style: normal;
    line-height: 21px;
  }
  .contact p {
    margin: 0;
  }
  .contact .gap {
    margin-top: 20px;
  }
  .footer-band {
    position: absolute;
    left: 0;
    bottom: 0;
    width: 927px;
    height: 80px;
    background: linear-gradient(90deg, var(--brand-blue) 0%, var(--green-light) 45%, var(--brand-green) 100%);
  }
  .website {
    position: absolute;
    right: 30px;
    bottom: 24px;
    color: var(--paper);
    font-size: 18px;
  }
</style>
</head>
<body>
  <main class="letterhead">
    <header class="brand">
      <span class="brand-mark"></span>
      <div class="brand-text">
        <span class="brand-name">Brightmoor Paving</span>
        <span class="brand-tagline">Synthetic Grass &amp; Softfall Rubber Surfaces</span>
      </div>
    </header>

    <address class="contact">
      <p>1234 Street, Bldg. 1</p>
      <p>City, State 12345</p>
      <p class="gap">P: (123) 456-7890</p>
      <p>F: (123) 456-7891</p>
    </address>

    <div class="footer-band" role="img" aria-label="Decorative blue and green footer band"></div>

    <span class="website">www.brightmoorpaving.com</span>
  </main>
</body>
</html>
```